Business card and Stationery for data intelligence company

We need a new design for our business cards and stationery (Business Letter templates and a Quote example on Word, but it MUST work on Google Doc as well).

We are a software company based in Ireland and UK. Our product is "Quarla", data intelligence platform with beautiful visualizations, graph capabilities (things are interconnected), powerful, flexible, it can manage Big Data and Streaming information. It's modern and relatively open source.
Our company will provide data intelligence for law enforcements, pharmaceuticals, and similar high end customers.

We'll launch a new website soon. At the moment it's http://www.quarla.tech if you want to take a look. This is our youtube channel in case you need it to understand what Quarla is: https://www.youtube.com/c/quarlatechchannel

We changed the logo so please use the logo I attach here.

We'd like the output to be cool and modern but elegant and "business" at the same time. It should inspire simple sophistication, "unity" "intent" "purpose" yet subtly very advanced and innovative.

The name "Quarla" does NOT refer to sirens (mithological creatures) as well as the warning devices. It means Quantum Unified Archival Record Layer Array. Please use our logo's colors and if you want to something like the "graph" image.

```html
<!DOCTYPE html>
<html lang="en">
<head>
<meta charset="utf-8">
<title>Quarla – Business Card</title>
<link rel="stylesheet" href="https://fonts.googleapis.com/css2?family=Lato:wght@400;700&display=swap">
<style>
  :root {
    --backdrop: #1077b3;
    --card-dark: #333132;
    --card-light: #ffffff;
    --brand-orange: #d97d27;
    --ink: #1e1e1e;
    --rule: #3a3a3a;
  }
  * { margin: 0; padding: 0; box-sizing: border-box; }
  html, body { width: 1200px; height: 1000px; overflow: hidden; }
  body {
    position: relative;
    background: var(--backdrop);
    font-family: "Lato", Arial, sans-serif;
    color: var(--ink);
  }
  .card { position: absolute; width: 570px; height: 393px; overflow: hidden; }
  .card-front { left: 315px; top: 92px; background: var(--card-dark); }
  .card-back { left: 314px; top: 515px; background: var(--card-light); }

  .brand { position: absolute; display: flex; align-items: center; }
  .brand-mark { border-radius: 50%; background: var(--brand-orange); flex: none; }
  .brand-name {
    color: var(--brand-orange);
    font-weight: 400;
    text-transform: uppercase;
    line-height: 1;
  }
  .card-front .brand { left: 127px; top: 153px; gap: 22px; }
  .card-front .brand-mark { width: 84px; height: 84px; }
  .card-front .brand-name { font-size: 54px; letter-spacing: 7px; }
  .card-back .brand { left: 30px; top: 38px; gap: 16px; }
  .card-back .brand-mark { width: 72px; height: 72px; }
  .card-back .brand-name { font-size: 40px; letter-spacing: 5px; }

  .holder {
    position: absolute; left: 31px; right: 30px; top: 221px;
    border-left: 2px solid var(--brand-orange);
    padding-left: 6px;
  }
  .holder-line { display: flex; align-items: flex-end; }
  .holder-name {
    font-size: 21px; font-weight: 700; color: var(--brand-orange);
    line-height: 23px; white-space: nowrap; flex: none;
  }
  .divider {
    flex: 1; margin: 0 0 3px 2px;
    border-top: 1.5px solid var(--rule);
  }
  .holder-role { font-size: 14px; font-weight: 700; line-height: 18px; }
  .address {
    position: absolute; right: 29px; top: 171px;
    text-align: right; font-size: 16px; line-height: 20px; font-style: normal;
  }
  .contacts {
    position: absolute; right: 30px; top: 285px;
    list-style: none; font-size: 16px; line-height: 20px;
  }
  .contacts li { display: flex; justify-content: flex-end; align-items: center; gap: 5px; }
  .contact-icon {
    width: 16px; height: 16px; background: var(--brand-orange);
    display: flex; align-items: center; justify-content: center;
  }
  .social { position: absolute; left: 29px; top: 327px; display: flex; gap: 4px; }
  .social span { width: 16px; height: 16px; background: var(--brand-orange); }
  .footer-bands { position: absolute; left: 0; bottom: 0; width: 570px; height: 36px; }
</style>
</head>
<body>
  <section class="card card-front" aria-label="Card front">
    <div class="brand">
      <span class="brand-mark"></span>
      <span class="brand-name">Quarla</span>
    </div>
  </section>

  <section class="card card-back" aria-label="Card back">
    <div class="brand">
      <span class="brand-mark"></span>
      <span class="brand-name">Quarla</span>
    </div>

    <address class="address">
      Unit 7<br>
      Harbourview Innovation Park<br>
      Eastfield, Corrib - Ireland
    </address>

    <div class="holder">
      <div class="holder-line">
        <p class="holder-name">Aiden Marlow</p>
        <span class="divider"></span>
      </div>
      <p class="holder-role">CEO</p>
    </div>

    <ul class="contacts">
      <li>+353 87 5550142
        <span class="contact-icon">
          <svg width="10" height="10" viewBox="0 0 10 10"><path d="M2 0.5 L3.6 0.5 L4.2 2.8 L3 3.6 Q4 5.8 6.4 7 L7.2 5.8 L9.5 6.4 L9.5 8 Q9.5 9.5 8 9.5 Q0.5 9 0.5 2 Q0.5 0.5 2 0.5Z" fill="#fff"/></svg>
        </span>
      </li>
      <li>www.quarla.tech
        <span class="contact-icon">
          <svg width="10" height="10" viewBox="0 0 10 10"><rect x="0.8" y="1" width="8.4" height="6" fill="none" stroke="#fff" stroke-width="1.2"/><rect x="3" y="8.2" width="4" height="1.1" fill="#fff"/></svg>
        </span>
      </li>
      <li>info@quarla.tech
        <span class="contact-icon">
          <svg width="10" height="8" viewBox="0 0 10 8"><rect x="0" y="0" width="10" height="8" fill="#fff"/><path d="M0 0 L5 4.5 L10 0" fill="none" stroke="#d97d27" stroke-width="1.1"/></svg>
        </span>
      </li>
    </ul>

    <div class="social" aria-label="Social links">
      <span></span><span></span><span></span>
    </div>

    <svg class="footer-bands" viewBox="0 0 570 36" aria-hidden="true">
      <polygon points="0,0 159,0 149,36 0,36" fill="var(--card-dark)"/>
      <polygon points="173,0 570,0 570,36 163,36" fill="var(--brand-orange)"/>
    </svg>
  </section>
</body>
</html>
```